Corvellan Solutions needs an IT Managed Services Website and the logo needs to be updated

We need a new website for our 25 year old IT Managed Services Company. Our company specializes in listening to and understanding our customer needs and goals. Our customers include SME's and Corporates in industries ranging from Medical, Legal, Industrial & Manufacturing and Financial. The services that we offer include: Managed IT Services, Remote Monitoring and Management and Virtualisation. Corvellan Solutions takes technology and makes the lives of our customers easier by applying it appropriately. In the same way, we want a website that is as pleasing to the eye, as it is simple to find information and call to action. The website should say as much in design as it does in content and it should be saying that Corvellan Solutions is your technology partner that listens to you, understands you, delivers solutions and is loyal in our relationship with you. Aesthetically, we want to go for something a little warmer than blue and white, but want to err on the side of professional.
The Logo: We need the "computer" and "ltd" to be removed from the logo. We want to keep the @ on the "u". We would like to freshen up the logo inline with the website design in terms of look and feel and colour.

Target Market(s)

Businesses that require IT Managed Services

Logo Text

Corvellan Solutions

Coding

Coded - Design and coding required

Number of Pages Required

5+ page

Font styles to use
Sans Serif

Colors

Designer to choose colors to be used in the design.

Requirements
Must have
• Each page must have a call to action.

```html
<!DOCTYPE html>
<html lang="en">
<head>
<meta charset="utf-8">
<title>Corvellan Solutions – IT Managed Services</title>
<link href="https://fonts.googleapis.com/css2?family=Poppins:wght@400;500;600&family=Lato:wght@400;700;900&display=swap" rel="stylesheet">
<style>
:root{
  --blue:#1e8ff0;
  --blue-dark:#0b6cc6;
  --ink:#231f1c;
  --body:#3d3733;
  --charcoal:#4a4441;
  --sand:#f4f0ea;
  --cream:#fbf8f3;
  --white:#ffffff;
  --teal:#1f6f86;
  --amber:#d99a55;
}
*{margin:0;padding:0;box-sizing:border-box}
html,body{width:1200px;height:3180px;overflow:hidden;background:var(--white)}
body{font-family:"Lato",sans-serif;color:var(--body);position:relative}
.heading{font-family:"Poppins",sans-serif}
a{color:inherit;text-decoration:none}

/* Navigation */
.site-nav{position:absolute;top:0;left:0;width:1200px;height:84px;background:var(--blue)}
.nav-links{position:absolute;top:0;height:84px;display:flex;align-items:center;gap:44px;font-weight:700;font-size:15px;color:var(--white)}
.nav-links.left{left:98px}
.nav-links.right{left:810px}
.nav-logo-tab{position:absolute;left:505px;top:0;width:240px;height:84px;background:var(--white);clip-path:polygon(0 0,100% 0,92% 100%,8% 100%);display:flex;align-items:center;justify-content:center}
.brand{display:flex;align-items:center;gap:8px;color:var(--teal);font-family:"Poppins",sans-serif;font-weight:500}
.brand .dot{width:26px;height:26px;border-radius:50%;background:var(--teal)}
.brand .name{font-size:28px;line-height:1}
.brand small{display:block;font-size:11px;text-align:right;margin-top:2px}

/* Hero */
.hero{position:absolute;top:84px;left:0;width:1200px;height:516px;
  background:
    radial-gradient(ellipse 420px 300px at 18% 40%,rgba(217,154,85,.45),transparent 70%),
    radial-gradient(ellipse 520px 380px at 75% 55%,rgba(150,185,215,.55),transparent 75%),
    linear-gradient(100deg,#4b4c52 0%,#6f7883 40%,#56677a 70%,#2f3a48 100%)}
.hero-title{position:absolute;left:98px;top:90px;font-size:74px;font-weight:600;color:var(--white);font-family:"Poppins",sans-serif}
.hero-quote{position:absolute;left:98px;top:200px;font-size:25px;font-weight:500;color:var(--white);font-family:"Poppins",sans-serif}
.hero-sub{position:absolute;left:98px;top:250px;width:540px;font-size:17px;line-height:1.35;color:var(--white)}
.hero-buttons{position:absolute;left:98px;top:332px;display:flex;gap:12px}
.btn{display:inline-block;padding:12px 20px;border-radius:24px;font-weight:700;font-size:15px;box-shadow:0 3px 6px rgba(0,0,0,.18)}
.btn-blue{background:var(--blue);color:var(--white)}
.btn-white{background:var(--white);color:var(--blue)}
.hero-arrow{position:absolute;top:230px}

/* Welcome */
.welcome{position:absolute;top:600px;left:0;width:1200px;height:568px;background:var(--cream)}
.welcome h2{position:absolute;left:98px;top:96px;font-size:33px;color:var(--ink);font-weight:500}
.welcome h1{position:absolute;left:98px;top:132px;font-size:58px;color:var(--blue);font-weight:600}
.welcome p{position:absolute;left:98px;top:228px;width:530px;font-size:13.5px;line-height:1.85;text-align:justify}
.welcome .btn{position:absolute;left:98px;top:398px}
.welcome-frame{position:absolute;left:752px;top:76px;width:350px;height:374px;border:3px solid #a49c94}
.welcome-photo{position:absolute;left:718px;top:100px;width:350px;height:376px;background:linear-gradient(140deg,#d3a774,#8a6a4e 45%,#4a4540 80%,#3a3f48)}

/* Services */
.services{position:absolute;top:1168px;left:0;width:1200px;height:557px}
.services-left{position:absolute;left:0;top:0;width:600px;height:557px;background:var(--charcoal)}
.services-right{position:absolute;left:600px;top:0;width:600px;height:557px;background:var(--sand)}
.services-left h3{position:absolute;left:98px;top:70px;font-size:26px;color:var(--white);font-weight:500}
.services-left h2{position:absolute;left:98px;top:100px;font-size:52px;color:var(--white);font-weight:600}
.service-tab{position:absolute;left:98px;width:438px;height:72px;border:3px solid var(--white);border-radius:36px;display:flex;align-items:center;gap:18px;padding-left:6px;font-size:20px;color:var(--white)}
.service-tab .ico{width:58px;height:58px;border-radius:50%;background:var(--white);display:flex;align-items:center;justify-content:center}
.service-tab.active{background:var(--white);color:var(--blue);border-color:var(--white)}
.service-tab.active .ico{background:var(--blue)}
.service-tab.active::after{content:"";position:absolute;right:-26px;top:16px;border-left:26px solid var(--white);border-top:18px solid transparent;border-bottom:18px solid transparent}
.services-right .s-icon{position:absolute;left:30px;top:48px}
.services-right h4{position:absolute;left:30px;top:148px;font-size:27px;color:var(--blue);font-weight:500}
.services-right .rule{position:absolute;left:30px;top:202px;width:112px;height:2px;background:var(--blue)}
.services-right p{position:absolute;left:30px;width:480px;font-size:13.5px;line-height:1.8}
.services-right .btn{position:absolute;left:32px;top:443px}

/* Why choose */
.why{position:absolute;top:1725px;left:0;width:1200px;height:588px;background:var(--white)}
.why-art{position:absolute;left:0;top:0;width:560px;height:588px;background:linear-gradient(90deg,#cfdceb 0%,#a9c6e4 30%,#dbe6f1 65%,rgba(255,255,255,0) 100%)}
.why h3{position:absolute;left:573px;top:86px;font-size:28px;color:var(--ink);font-weight:500}
.why h2{position:absolute;left:573px;top:120px;font-size:50px;color:var(--blue);font-family:"Poppins",sans-serif;font-weight:600}
.why p{position:absolute;left:573px;width:528px;font-size:13.5px;line-height:1.8;text-align:justify}
.why .btn{position:absolute;left:573px;top:458px}

/* Engineers band */
.team{position:absolute;top:2313px;left:0;width:1200px;height:430px;background:linear-gradient(90deg,#ece9e4 0%,#dfe5e8 50%,#bccfdb 100%)}
.team-art{position:absolute;right:0;top:0;width:520px;height:430px;background:linear-gradient(90deg,rgba(188,207,219,0) 0%,#c8d8e3 35%,#e9eff3 65%,#aac0cf 100%)}
.team p{position:absolute;left:98px;width:555px;font-size:14px;line-height:1.8;color:var(--ink);text-align:justify}

/* Footer */
.footer{position:absolute;top:2743px;left:0;width:1200px;height:437px;background:var(--white)}
.footer .brand{position:absolute;left:488px;top:85px}
.footer .brand .name{font-size:40px}
.footer .brand .dot{width:34px;height:34px}
.socials{position:absolute;left:496px;top:200px;display:flex;gap:10px}
.socials span{width:38px;height:38px;border:2px solid var(--ink);border-radius:50%;display:flex;align-items:center;justify-content:center}
.footer-nav{position:absolute;left:215px;top:290px;display:flex;gap:38px;font-size:15px;font-weight:700;color:var(--ink)}
.footer-nav .sep{font-weight:400}
.footer-rule{position:absolute;left:98px;top:357px;width:1004px;height:1px;background:#d6d0c8}
.copyright{position:absolute;left:0;width:1200px;top:388px;text-align:center;font-size:14px;font-weight:700;color:var(--ink)}
</style>
</head>
<body>

<header class="site-nav">
  <nav class="nav-links left"><a>HOME</a><a>ABOUT US</a><a>SERVICES</a></nav>
  <div class="nav-logo-tab">
    <div class="brand"><span class="dot"></span><div><span class="name">Corvellan</span><small>Solutions</small></div></div>
  </div>
  <nav class="nav-links right"><a>WHY US</a><a>BLOG</a><a>CONTACT US</a></nav>
</header>

<section class="hero" role="img" aria-label="Blurred photo of a person using a tablet surrounded by a network of connected device icons">
  <h1 class="hero-title">Corvellan</h1>
  <p class="hero-quote">"Free choices become the matrix of human life"</p>
  <p class="hero-sub">An environment in which something develops; a surrounding medium or structure.</p>
  <div class="hero-buttons"><a class="btn btn-blue">Remote Assistance for PC</a><a class="btn btn-white">Remote Assistance for Orchard</a></div>
  <svg class="hero-arrow" style="left:36px" width="30" height="52" viewBox="0 0 30 52"><path d="M26 2 4 26l22 24" fill="none" stroke="#fff" stroke-width="3"/></svg>
  <svg class="hero-arrow" style="left:1136px" width="30" height="52" viewBox="0 0 30 52"><path d="M4 2l22 24L4 50" fill="none" stroke="#fff" stroke-width="3"/></svg>
</section>

<section class="welcome">
  <h2 class="heading">Welcome To</h2>
  <h1 class="heading">Corvellan</h1>
  <p>Corvellan Solutions is an IT Managed Services Provider (MSP) that has more than 25 years experience growing and collaborating in the IT Industry. Our expertise lies in listening to and understanding our more than 1000 customers' needs and delivering the best value for money IT Infrastructure and Technology solutions. We believe in loyal and lasting relationships creating a matrix within which your company can grow and outperform it's own expectations.</p>
  <a class="btn btn-blue">Read More</a>
  <div class="welcome-frame"></div>
  <div class="welcome-photo" role="img" aria-label="Photo of a team working together around a table with laptops, seen from above"></div>
</section>

<section class="services">
  <div class="services-left">
    <h3 class="heading">How can we can help you?</h3>
    <h2 class="heading">Our Services</h2>
    <div class="service-tab active" style="top:222px"><span class="ico"><svg width="30" height="34" viewBox="0 0 30 34"><circle cx="15" cy="9" r="7" fill="#fff"/><path d="M2 34c0-9 6-14 13-14s13 5 13 14z" fill="#fff"/></svg></span>Managed IT Services</div>
    <div class="service-tab" style="top:308px"><span class="ico"><svg width="32" height="32" viewBox="0 0 32 32"><circle cx="16" cy="16" r="9" fill="none" stroke="#333" stroke-width="3" stroke-dasharray="4 3"/><circle cx="16" cy="16" r="4" fill="#333"/></svg></span>Remote Monitoring &amp; Management</div>
    <div class="service-tab" style="top:394px"><span class="ico"><svg width="32" height="32" viewBox="0 0 32 32"><path d="M6 28V16a10 10 0 0 1 20-2l2 6h-3v5h-6v3" fill="none" stroke="#333" stroke-width="2.5"/><circle cx="16" cy="14" r="3" fill="#333"/></svg></span>Virtualisation</div>
  </div>
  <div class="services-right">
    <svg class="s-icon" width="66" height="80" viewBox="0 0 66 80"><circle cx="33" cy="20" r="16" fill="#1e8ff0"/><path d="M4 80c0-22 12-36 29-36s29 14 29 36z" fill="#1e8ff0"/><path d="M33 46l-5 8 5 18 5-18z" fill="#fff"/></svg>
    <h4 class="heading">Managed IT Services</h4>
    <div class="rule"></div>
    <p style="top:240px">Corvellan brings a personal touch to you through our IT consulting services. We collaborate with partners across the globe to bring the best technology to you. You can rely on our expertise to design and maintain the most effective infrastructure for your business.</p>
    <p style="top:353px">Our quick and efficient Support team will troubleshoot your IT problems and ensure your business continues to operate with minimum disruption.</p>
    <a class="btn btn-blue">Contact Us Now</a>
  </div>
</section>

<section class="why">
  <div class="why-art" role="img" aria-label="Illustration of a blue padlock surrounded by circular digital circuit patterns"></div>
  <h3 class="heading">Corvellan Solutions</h3>
  <h2>Why Choose Us</h2>
  <p style="top:210px">Corvellan Solutions was founded in 2000 and is in the business of collaborating with partners to bring the best technologies to you.</p>
  <p style="top:262px">We have more than 25 years experience in the IT industry, servicing customers across the GTA and Ontario. Our customers come from different industry sectors including Medical, Financial, Real Estate, Legal and more. We work together with our customers as members of their teams to realize their IT visions and goals.</p>
  <p style="top:372px">We have collaborated with partners across the globe to ensure that we bring the most innovate and functional technology to our customers. We can proudly say that we offer the best Value for Money solutions.</p>
  <a class="btn btn-blue">Read More</a>
</section>

<section class="team">
  <div class="team-art" role="img" aria-label="Futuristic close-up image with glowing holographic rings"></div>
  <p style="top:98px">Our engineers are highly skilled and we invest time and money in ensuring they are up to date on the latest technologies so as to better support our customers. We ensure that we are proactive and communicating effectively. In times of crisis, it is not only about resolving the problem, but also about communicating effectively and ensuring that our customers know that we are right there beside them.</p>
  <p style="top:262px">You need a loyal and committed partner like Corvellan who can solve problems and help to ensure that your IT infrastructure is secure and operating beyond expectations for the long term.</p>
</section>

<footer class="footer">
  <div class="brand"><span class="dot"></span><div><span class="name">Corvellan</span><small>Solutions</small></div></div>
  <div class="socials" aria-label="Contact links">
    <span><svg width="18" height="18" viewBox="0 0 18 18"><path d="M2 4h14v10H2z M2 4l7 6 7-6" fill="none" stroke="#231f1c" stroke-width="1.6"/></svg></span>
    <span><svg width="18" height="18" viewBox="0 0 18 18"><path d="M4 2h3l1.5 4-2 1.2a9 9 0 0 0 4.3 4.3L12 9.5l4 1.5v3a2 2 0 0 1-2 2A12 12 0 0 1 2 4a2 2 0 0 1 2-2z" fill="#231f1c"/></svg></span>
    <span><svg width="18" height="18" viewBox="0 0 18 18"><path d="M9 1a5.5 5.5 0 0 0-5.5 5.5C3.5 11 9 17 9 17s5.5-6 5.5-10.5A5.5 5.5 0 0 0 9 1z" fill="#231f1c"/><circle cx="9" cy="6.5" r="2" fill="#fff"/></svg></span>
    <span><svg width="18" height="18" viewBox="0 0 18 18"><circle cx="9" cy="9" r="7" fill="none" stroke="#231f1c" stroke-width="1.6"/><path d="M2 9h14M9 2c3 3.5 3 10.5 0 14M9 2c-3 3.5-3 10.5 0 14" fill="none" stroke="#231f1c" stroke-width="1.4"/></svg></span>
    <span><svg width="18" height="18" viewBox="0 0 18 18"><circle cx="4" cy="9" r="2.2" fill="#231f1c"/><circle cx="14" cy="4" r="2.2" fill="#231f1c"/><circle cx="14" cy="14" r="2.2" fill="#231f1c"/><path d="M4 9l10-5M4 9l10 5" stroke="#231f1c" stroke-width="1.5"/></svg></span>
  </div>
  <nav class="footer-nav"><a>HOME</a><span class="sep">|</span><a>ABOUT US</a><span class="sep">|</span><a>SERVICES</a><span class="sep">|</span><a>WHY US</a><span class="sep">|</span><a>BLOG</a><span class="sep">|</span><a>CONTACT US</a></nav>
  <div class="footer-rule"></div>
  <p class="copyright">Copyrights @ 2018 Corvellan. All Rights Reserved.</p>
</footer>

</body>
</html>
```